I need a fresh looking, exciting and loaded design for Full service Restaurant

We need a web design for our restaurant, which offers full service Pakistani and Indian food in PA, USA. Design should be elegant, simplified so customers can navigate easily and order food online for catering as well as delivery. We need loads of pictures and room to grow. I already have a web address via vexlorin.com. It should include SSL and e-commerce for ordering food.
Be original and be creative and make it a fun site :)

Industry/Entity Type

Restaurant

```html
<!DOCTYPE html>
<html lang="en">
<head>
<meta charset="utf-8">
<title>Masala Haveli – Pak-Indian Cuisine</title>
<link href="https://fonts.googleapis.com/css2?family=Raleway:wght@500;600;700&family=Lato:wght@400;700&display=swap" rel="stylesheet">
<style>
:root{
  --red:#d91f26;
  --red-deep:#c8161d;
  --ink:#1b1b1b;
  --grey-bg:#f1f1f1;
  --line:#8a8a8a;
  --white:#ffffff;
  --dark-tile:#1e1e1e;
}
*{box-sizing:border-box;margin:0;padding:0}
html,body{width:1200px;height:2965px;overflow:hidden}
body{position:relative;background:var(--white);font-family:'Lato',sans-serif;color:var(--ink)}
.abs{position:absolute}
.diamond{position:absolute;transform:rotate(45deg);overflow:hidden}

/* nav */
.topbar{left:0;top:0;width:1200px;height:55px;background:var(--red);color:var(--white);font-size:12px;font-weight:700;letter-spacing:.3px}
.topbar ul{position:absolute;top:0;height:55px;display:flex;align-items:center;list-style:none}
.topbar li{display:flex;align-items:center}
.topbar li+li::before{content:"|";margin:0 21px;opacity:.9}
.nav-main{left:49px}
.nav-user{right:55px}

/* hero */
.hero{left:0;top:55px;width:1200px;height:578px;background:radial-gradient(ellipse at 50% 45%,#c9a477 0%,#e3cfb3 40%,#efe3d2 75%,#e8d6bd 100%)}
.hero-side{top:0;width:200px;height:578px;background:linear-gradient(180deg,#f4ece2,#e6d3b8)}
.hero-diamond{width:247px;height:247px;background:var(--red)}
.hero-diamond-inner{position:absolute;inset:0;transform:rotate(-45deg);display:flex;align-items:center;justify-content:center}
.brand{left:400px;top:98px;width:400px;text-align:center}
.brand-name{display:flex;align-items:center;justify-content:center;gap:12px;font-family:'Raleway',sans-serif;font-weight:700;font-size:46px;color:var(--red-deep)}
.brand-dot{width:20px;height:20px;border-radius:50%;background:#2c7a2a}
.brand-tag{font-family:'Raleway',sans-serif;font-weight:600;font-size:15px;color:var(--red-deep);margin-top:2px}
.btn-order{left:461px;top:297px;width:284px;height:69px;background:var(--red);color:var(--white);font-family:'Raleway',sans-serif;font-weight:500;font-size:28px;display:flex;align-items:center;justify-content:center;gap:22px}

/* welcome */
.welcome{left:0;top:633px;width:1200px;height:666px;background:var(--grey-bg)}
.section-title{position:absolute;left:0;width:1200px;text-align:center;font-family:'Raleway',sans-serif;font-weight:700;font-size:33px}
.section-title .accent{color:var(--red)}
.lede{position:absolute;left:125px;width:950px;text-align:center;font-size:12px;line-height:21px;color:#444}
.timeline{left:585px;top:197px;width:2px;height:380px;background:var(--line)}
.branch{height:2px;background:var(--line)}
.knot{width:12px;height:12px;background:var(--red);transform:rotate(45deg)}
.cuisine{font-family:'Lato',sans-serif;text-align:center}
.cuisine b{display:block;font-weight:400;font-size:35px;color:var(--red);line-height:36px}
.cuisine span{display:block;font-size:27px;color:var(--ink);line-height:34px}

/* popular */
.popular{left:0;top:1299px;width:1200px;height:718px;background:radial-gradient(ellipse at 55% 60%,#e8454a 0%,var(--red) 55%,#cf1c23 100%);color:var(--white)}
.popular .section-title{color:var(--white)}
.popular .lede{color:#fff}
.dish-tile{width:124px;height:124px;border:3px solid var(--white)}
.dish-tile-feature{background:var(--dark-tile)}
.feature-text{position:absolute;inset:0;transform:rotate(-45deg);display:flex;flex-direction:column;align-items:center;justify-content:center;text-align:center;color:var(--white)}
.feature-text h3{font-family:'Raleway',sans-serif;font-weight:500;font-size:23px}
.feature-text p{font-size:10px;line-height:13px;margin-top:4px;width:120px}

/* order */
.order-band{left:0;top:2017px;width:1200px;height:500px;background:linear-gradient(135deg,#e9e0d3,#f3ede4 45%,#d9c7ad)}
.order-strip{left:0;top:2017px;width:1200px;height:36px;background:#f4f4f4}
.order-panel{left:115px;top:2078px;width:968px;height:405px;background:rgba(255,255,255,.94);border:1px solid #b9b9b9}
.panel-divider{left:484px;top:34px;width:1px;height:338px;background:#cfcfcf}
.panel-title{position:absolute;font-family:'Lato',sans-serif;font-size:28px;text-align:center}
.panel-title .accent{color:var(--red)}
.special-tile{width:105px;height:105px;border:3px solid var(--white)}
.field{position:absolute;left:547px;width:354px;height:32px;background:var(--white);border:1px solid #c8c8c8;box-shadow:0 1px 2px rgba(0,0,0,.15);font-size:12px;color:#555;padding-left:12px;display:flex;align-items:center}
.field::after{content:"";position:absolute;right:12px;top:13px;border:4px solid transparent;border-top:5px solid #333}
.btn-book{left:547px;top:304px;width:354px;height:58px;background:var(--red);color:var(--white);font-family:'Lato',sans-serif;font-weight:700;font-size:28px;display:flex;align-items:center;justify-content:center;letter-spacing:.5px}

/* testimonials */
.testimonials{left:0;top:2517px;width:1200px;height:386px;background:var(--red);color:var(--white)}
.quote-badge{left:549px;top:31px;width:72px;height:72px;border:2px solid var(--white);border-radius:50%;display:flex;align-items:center;justify-content:center}
.quote-badge span{width:46px;height:46px;border-radius:50%;background:var(--white);display:flex;align-items:center;justify-content:center}
.testimonials .section-title{font-weight:500;font-size:28px;color:var(--white)}
.quote{position:absolute;left:100px;width:1000px;text-align:center;font-size:13px;font-weight:700;line-height:30px}
.author{left:430px;top:2292px;width:340px}
.author-row{left:430px;top:280px;width:340px;display:flex;align-items:center;gap:14px;font-size:17px}
.author-row i{flex:1;height:1px;background:rgba(255,255,255,.85)}
.dots{left:558px;top:326px;display:flex;gap:8px}
.dots i{width:11px;height:11px;border:2px solid var(--white);border-radius:50%}
.dots i.on{background:var(--white)}

/* footer */
.footer{left:0;top:2903px;width:1200px;height:62px;background:var(--white)}
.copyright{left:51px;top:24px;font-size:13px;color:#333}
.social{right:52px;top:24px;display:flex;gap:22px}
.social i{width:14px;height:14px;border-radius:50%;background:#3a3a3a}
.social i.first{background:var(--red)}
</style>
</head>
<body>

<header class="abs topbar">
  <ul class="nav-main"><li>HOME</li><li>EVENTS</li><li>MENU</li><li>GALLERY</li><li>CONTACTS</li></ul>
  <ul class="nav-user"><li>MY ACCOUNT</li><li>MY WISHLIST</li><li>CHECKOUT</li><li>LOGIN</li></ul>
</header>

<section class="abs hero" role="img" aria-label="Photograph of Pakistani and Indian curries in serving bowls">
  <div class="abs hero-side" style="left:0;background:linear-gradient(135deg,#fbf8f4 0 48%,#e8d7bf 52%)"></div>
  <div class="abs hero-side" style="right:0;background:linear-gradient(225deg,#fbf8f4 0 48%,#e3d2b8 52%)"></div>

  <div class="diamond hero-diamond" style="left:86px;top:156px">
    <div class="hero-diamond-inner">
      <svg width="120" height="140" viewBox="0 0 120 140" fill="none" stroke="#fff" stroke-width="9" stroke-linejoin="round">
        <rect x="34" y="8" width="66" height="112" rx="10"/>
        <line x1="56" y1="22" x2="78" y2="22" stroke-linecap="round"/>
        <circle cx="67" cy="106" r="4" fill="#fff" stroke="none"/>
        <path d="M34 70 L14 96 L14 132 L60 132 L60 120" stroke-linecap="round"/>
      </svg>
    </div>
  </div>

  <div class="diamond hero-diamond" style="left:866px;top:156px">
    <div class="hero-diamond-inner">
      <svg width="120" height="100" viewBox="0 0 120 100" fill="#fff">
        <circle cx="60" cy="14" r="7"/>
        <path d="M14 72 A46 46 0 0 1 106 72 Z"/>
        <rect x="6" y="78" width="108" height="9" rx="3"/>
      </svg>
    </div>
  </div>

  <div class="abs brand">
    <div class="brand-name"><span class="brand-dot"></span>Masala Haveli</div>
    <div class="brand-tag">A fine Pak-Indian Cuisine</div>
  </div>

  <a class="abs btn-order">ORDER NOW
    <svg width="14" height="20" viewBox="0 0 14 20"><path d="M2 2 L11 10 L2 18" stroke="#fff" stroke-width="3.5" fill="none"/></svg>
  </a>
</section>

<section class="abs welcome">
  <h2 class="section-title" style="top:44px">WELCOME TO <span class="accent">MASALA HAVELI</span></h2>
  <p class="lede" style="top:114px">Lorem ipsum dolor sit amet, consectetur adipiscing elit, sed do eiusmod tempor incididunt ut labore et dolore magna aliqua. Ut enim ad minim veniam, quis nostrud exercitation ullamco laboris nisi ut aliquip ex ea commodo consequat. Duis aute irure dolor in reprehenderit in voluptate velit esse cillum dolore eu fugiat nulla pariatur. Excepteur sint occaecat cupidatat non proident, sunt in culpa qui officia deserunt mollit anim id est laborum.</p>

  <div class="abs timeline"></div>
  <div class="abs branch" style="left:433px;top:316px;width:147px"></div>
  <div class="abs knot" style="left:580px;top:311px"></div>
  <div class="abs branch" style="left:592px;top:450px;width:160px"></div>
  <div class="abs knot" style="left:580px;top:445px"></div>

  <div class="diamond" role="img" aria-label="Photograph of Indian chicken biryani" style="left:261px;top:245px;width:142px;height:142px;background:radial-gradient(circle,#d9a24a,#b86a2a 60%,#8d5228)"></div>
  <div class="abs cuisine" style="left:232px;top:422px;width:200px"><b>INDIAN</b><span>Dishes</span></div>

  <div class="abs cuisine" style="left:740px;top:276px;width:200px"><b>PAKISTANI</b><span>Dishes</span></div>
  <div class="diamond" role="img" aria-label="Photograph of Pakistani rice and chicken dish" style="left:773px;top:379px;width:142px;height:142px;background:radial-gradient(circle,#f2c64a,#c77a2c 55%,#5a3a22)"></div>
</section>

<section class="abs popular">
  <h2 class="section-title" style="top:42px">POPULAR DISHES</h2>
  <p class="lede" style="top:91px;left:120px;width:960px">Lorem ipsum dolor sit amet, consectetur adipiscing elit, sed do eiusmod tempor incididunt ut labore et dolore magna aliqua. Ut enim ad minim veniam, quis nostrud exercitation ullamco laboris nisi ut aliquip ex ea commodo consequat. Duis aute irure dolor in reprehenderit in voluptate velit esse cillum dolor</p>

  <div class="abs" style="left:595px;top:154px;width:2px;height:52px;background:rgba(255,255,255,.8)"></div>
  <div class="diamond" style="left:568px;top:206px;width:54px;height:54px;border:2px solid #fff">
    <svg style="position:absolute;inset:0;transform:rotate(-45deg)" width="50" height="50" viewBox="0 0 50 50" fill="#fff">
      <circle cx="25" cy="15" r="2.5"/><path d="M13 30 A12 12 0 0 1 37 30 Z"/><rect x="11" y="32" width="28" height="3" rx="1"/>
    </svg>
  </div>

  <div class="diamond dish-tile" role="img" aria-label="Photograph of samosas" style="left:433px;top:286px;background:radial-gradient(circle,#e6b46a,#b8793a)"></div>
  <div class="diamond dish-tile" role="img" aria-label="Photograph of kebabs with chutney" style="left:638px;top:286px;background:radial-gradient(circle,#c9553d,#6e3e2b)"></div>
  <div class="diamond dish-tile" role="img" aria-label="Photograph of rice on a banana leaf" style="left:337px;top:394px;background:radial-gradient(circle,#f1efe6,#5f8a3a)"></div>
  <div class="diamond dish-tile dish-tile-feature" style="left:535px;top:375px">
    <div class="feature-text">
      <h3>Chicken</h3>
      <p>Lorem ipsum dolor sit amet, consectetur</p>
      <svg style="margin-top:8px" width="18" height="18" viewBox="0 0 18 18"><circle cx="9" cy="9" r="9" fill="#fff"/><path d="M7 5 L11 9 L7 13" stroke="#1e1e1e" stroke-width="2.2" fill="none"/></svg>
    </div>
  </div>
  <div class="diamond dish-tile" role="img" aria-label="Photograph of grilled chicken pieces" style="left:732px;top:390px;background:radial-gradient(circle,#d89a52,#8a5a2e)"></div>
  <div class="diamond dish-tile" role="img" aria-label="Photograph of stuffed aubergine" style="left:433px;top:500px;background:radial-gradient(circle,#a65a2e,#4f4a2a)"></div>
  <div class="diamond dish-tile" role="img" aria-label="Photograph of seekh kebab skewers" style="left:638px;top:500px;background:radial-gradient(circle,#d4844c,#9a4a2a)"></div>
</section>

<section class="abs order-band" role="img" aria-label="Photograph of onion rings and salad on a table"></section>
<div class="abs order-strip"></div>
<section class="abs order-panel">
  <h3 class="panel-title" style="left:0;top:24px;width:484px">Today Special <span class="accent">Dishes</span></h3>
  <div class="diamond special-tile" role="img" aria-label="Photograph of fried chicken" style="left:116px;top:94px;background:radial-gradient(circle,#c5773a,#7a3e1c)"></div>
  <div class="diamond special-tile" role="img" aria-label="Photograph of curry chicken" style="left:296px;top:94px;background:radial-gradient(circle,#d69a3a,#8a5322)"></div>
  <div class="diamond special-tile" role="img" aria-label="Photograph of tandoori chicken" style="left:207px;top:175px;background:radial-gradient(circle,#a8573a,#5a2c1c)"></div>
  <div class="diamond special-tile" role="img" aria-label="Photograph of raita salad" style="left:106px;top:254px;background:radial-gradient(circle,#e8ecdc,#7f9c6a)"></div>
  <div class="diamond special-tile" role="img" aria-label="Photograph of korma curry" style="left:307px;top:254px;background:radial-gradient(circle,#e7a23c,#a5561c)"></div>

  <div class="abs panel-divider"></div>

  <h3 class="panel-title" style="left:484px;top:36px;width:484px">ONLINE <span class="accent">ORDER</span></h3>
  <div class="field" style="top:89px">Select Food Items</div>
  <div class="field" style="top:142px">Select Food</div>
  <div class="field" style="top:195px">Name</div>
  <div class="field" style="top:249px">Address</div>
  <a class="abs btn-book">BOOKING</a>
</section>

<section class="abs testimonials">
  <div class="abs quote-badge"><span>
    <svg width="24" height="22" viewBox="0 0 24 22"><path d="M2 2 H22 V15 H10 L5 20 V15 H2 Z" fill="var(--red)"/><circle cx="9" cy="8.5" r="1.8" fill="#fff"/><circle cx="15" cy="8.5" r="1.8" fill="#fff"/></svg>
  </span></div>
  <h2 class="section-title" style="top:108px">CLIENT TESTIMONIALS</h2>
  <p class="quote" style="top:210px">Lorem ipsum dolor sit amet, consectetur adipiscing elit, sed do eiusmod tempor incididunt ut labore et dolore magna aliqua. Ut enim ad minim veniam,<br>quis nostrud exercitation ullamco laboris nisi ut aliquip ex ea commodo consequat.</p>
  <div class="abs author-row"><i></i>Daniel Rowe<i></i></div>
  <div class="abs dots"><i></i><i class="on"></i><i></i></div>
</section>

<footer class="abs footer">
  <p class="abs copyright">All Rights Reserved. Copyrights @company Name. 2016</p>
  <div class="abs social"><i class="first"></i><i></i><i></i><i></i><i></i></div>
</footer>

</body>
</html>
```